Need Business Cards, Letterhead, and Stationary

Hi, please design a full stationary set for the attached logo (Business Cards, Letterhead, A4 Envelope, and other important stationary items that you can think of)
Please be as creative as you wish. The logo is for An Entrepreneurship Academy that teaches young and starting Entrepreneur skills they need to start their business.

```html
<!DOCTYPE html>
<html lang="en">
<head>
<meta charset="utf-8">
<title>Grove Startup Academy – Presentation Folder</title>
<link rel="stylesheet" href="https://fonts.googleapis.com/css2?family=Ubuntu:wght@400;500;700&display=swap">
<style>
  :root {
    --backdrop: #d4d4d4;
    --folder-black: #0e0e0e;
    --fold-line: #2a2a2a;
    --ink-white: #f2f2f2;
    --ink-muted: #7a7a7a;
    --brand-yellow: #f2c200;
    --brand-grey: #6d6e71;
    --brand-blue: #0d67a6;
    --brand-white: #f4f4f4;
  }
  * { margin: 0; padding: 0; box-sizing: border-box; }
  html, body {
    width: 1200px;
    height: 900px;
    overflow: hidden;
    background: var(--backdrop);
    font-family: "Ubuntu", sans-serif;
  }
  .folder {
    position: absolute;
    left: 81px;
    top: 90px;
    width: 1039px;
    height: 718px;
    display: flex;
  }
  .folder-panel {
    position: relative;
    height: 100%;
    background: var(--folder-black);
  }
  .folder-panel--back { width: 519px; }
  .folder-panel--front {
    width: 520px;
    border-left: 1px solid var(--fold-line);
  }
  .contact-block {
    position: absolute;
    left: 17px;
    bottom: 18px;
    color: var(--ink-white);
    font-size: 8px;
    line-height: 10px;
  }
  .contact-block__org {
    color: var(--ink-muted);
    font-size: 6.5px;
    margin-bottom: 3px;
  }
  .contact-block__numbers {
    display: flex;
    align-items: center;
    gap: 7px;
    margin-top: 5px;
  }
  .contact-block__number {
    display: flex;
    align-items: center;
    gap: 4px;
  }
  .contact-block__icon { width: 9px; height: 9px; }
  .brand-lockup {
    position: absolute;
    left: 90px;
    top: 128px;
    display: flex;
    align-items: center;
    gap: 18px;
    color: var(--ink-white);
    font-weight: 700;
  }
  .brand-lockup__dot {
    width: 70px;
    height: 70px;
    border-radius: 50%;
    background: var(--brand-blue);
  }
  .brand-lockup__name {
    font-size: 60px;
    line-height: 56px;
    letter-spacing: 1px;
  }
  .brand-lockup__sub {
    display: block;
    font-size: 13.5px;
    line-height: 18px;
    letter-spacing: 1.2px;
    text-transform: uppercase;
  }
  .web-address {
    position: absolute;
    left: 185px;
    bottom: 18px;
    width: 150px;
    text-align: center;
    color: var(--ink-white);
    font-size: 9px;
    font-weight: 700;
    letter-spacing: 0.4px;
  }
  .colour-bar {
    position: absolute;
    left: 185px;
    bottom: 0;
    width: 151px;
    height: 8px;
    display: flex;
  }
  .colour-bar span { flex: 1; }
  .colour-bar .yellow { background: var(--brand-yellow); }
  .colour-bar .grey { background: var(--brand-grey); }
  .colour-bar .blue { background: var(--brand-blue); }
  .colour-bar .white { background: var(--brand-white); }
</style>
</head>
<body>
  <main class="folder">
    <section class="folder-panel folder-panel--back">
      <address class="contact-block" style="font-style: normal;">
        <p class="contact-block__org">Grove Startup Academy</p>
        <p>Office Building Street</p>
        <p>City, 00000 Country</p>
        <div class="contact-block__numbers">
          <span class="contact-block__number">
            <svg class="contact-block__icon" viewBox="0 0 10 10" aria-hidden="true">
              <rect x="1" y="0.5" width="8" height="9" rx="1" fill="none" stroke="#bbb" stroke-width="1"/>
              <rect x="2.5" y="2" width="5" height="3" fill="#bbb"/>
            </svg>
            000 0000 0000
          </span>
          <span class="contact-block__number">
            <svg class="contact-block__icon" viewBox="0 0 10 10" aria-hidden="true">
              <rect x="0.5" y="4" width="9" height="5" rx="1" fill="none" stroke="#bbb" stroke-width="1"/>
              <path d="M2.5 4V1h5v3" fill="none" stroke="#bbb" stroke-width="1"/>
            </svg>
            000 0000 0000
          </span>
        </div>
      </address>
    </section>
    <section class="folder-panel folder-panel--front">
      <div class="brand-lockup">
        <span class="brand-lockup__dot" aria-hidden="true"></span>
        <div>
          <span class="brand-lockup__name">GROVE</span>
          <span class="brand-lockup__sub">Startup Academy</span>
        </div>
      </div>
      <p class="web-address">www.gsa-demo.com</p>
      <div class="colour-bar" aria-hidden="true">
        <span class="yellow"></span><span class="grey"></span><span class="blue"></span><span class="white"></span>
      </div>
    </section>
  </main>
</body>
</html>
```